Marta Business Card

My wife is going to start her own business with renting holiday appartments to tourists. She needs a design for a new business card... and a new web site.
Look at Stayvolt "Erholung auf dem Lindenwäldchen"

Target Market(s)

Give business card to prospects at any situation

Contact Information for Business Card

not sure what this means

Font styles to use
Script

Colors
fec41a
fee18a

Requirements
Must have
• My wife's handwriting is difficult to read:
Entspannen - Loslassen - Auftanken
Marta & das Lindenwäldchen
Urlaub an einem besonderen Ort
Marta Brecke
Grauer Pfad 7
18471 Alt Feldow
post@marta-brecke.de
www.lindenwaeldchen.net
Nice to have
• Beige background
Font like handwriting

```html
<!DOCTYPE html>
<html lang="de">
<head>
<meta charset="utf-8">
<title>Marta &amp; das Lindenwäldchen – Visitenkarte</title>
<link rel="stylesheet" href="https://fonts.googleapis.com/css2?family=Marcellus&family=Parisienne&display=swap">
<style>
  :root {
    --page: #ffffff;
    --card-yellow: #fbe87a;
    --card-white: #ffffff;
    --accent-line: #fbe87a;
    --ink: #2a1710;
    --shadow: rgba(0, 0, 0, 0.28);
  }
  * { margin: 0; padding: 0; box-sizing: border-box; }
  html, body {
    width: 1200px; height: 1000px; overflow: hidden;
    background: var(--page);
  }
  .canvas { position: relative; width: 1200px; height: 1000px; }
  .card {
    position: absolute; left: 245px; width: 709px; height: 405px;
    box-shadow: 2px 3px 6px var(--shadow);
    color: var(--ink);
    font-family: "Marcellus", serif;
  }
  .card--front { top: 71px; background: var(--card-yellow); }
  .card--back { top: 522px; background: var(--card-white); }

  .tagline {
    position: absolute; top: 58px; left: 0; width: 100%;
    text-align: center; font-size: 29px; letter-spacing: 0.3px;
    white-space: nowrap;
  }
  .brand-name {
    font-family: "Parisienne", cursive; font-weight: 400; line-height: 1;
    white-space: nowrap;
  }
  .card--front .brand-name {
    position: absolute; top: 168px; left: 0; width: 100%;
    text-align: center; font-size: 52px;
  }
  .card--front .brand-claim {
    position: absolute; top: 242px; left: 0; width: 100%;
    text-align: center; font-size: 24px; white-space: nowrap;
  }

  .divider { position: absolute; background: var(--accent-line); width: 4px; }
  .divider--upper { left: 348px; top: 0; height: 302px; }
  .divider--lower { left: 356px; top: 101px; bottom: 0; }

  .back-brand {
    position: absolute; right: 400px; top: 102px; text-align: right;
  }
  .back-brand .brand-name { display: block; font-size: 38px; line-height: 46px; }
  .back-brand .brand-claim { display: block; margin-top: 8px; font-size: 17px; white-space: nowrap; }

  .contact { position: absolute; left: 405px; top: 102px; white-space: nowrap; }
  .contact-name { font-size: 33px; font-weight: 400; letter-spacing: 0.3px; }
  .contact-block { font-size: 23px; line-height: 27px; font-style: normal; }
  .contact-address { margin-top: 22px; }
  .contact-online { margin-top: 27px; }
</style>
</head>
<body>
<div class="canvas">
  <section class="card card--front">
    <p class="tagline">Entspannen - Loslassen – Auftanken</p>
    <h1 class="brand-name">Marta &amp; das Lindenwäldchen</h1>
    <p class="brand-claim">Urlaub an einem besonderen Ort</p>
  </section>

  <section class="card card--back">
    <span class="divider divider--upper"></span>
    <span class="divider divider--lower"></span>
    <div class="back-brand">
      <span class="brand-name">Marta &amp;<br>das Lindenwäldchen</span>
      <span class="brand-claim">Urlaub an einem besonderen Ort</span>
    </div>
    <div class="contact">
      <h2 class="contact-name">MARTA BRECKE</h2>
      <address class="contact-block contact-address">Grauer Pfad 7<br>18471 Alt Feldow</address>
      <p class="contact-block contact-online">post@marta-brecke.de<br>www.lindenwaeldchen.net</p>
    </div>
  </section>
</div>
</body>
</html>
```